Lending Harbor Partners - business cards

we need new business cards for my company.
i've been in business for 25 years.
my wife and I are mortgage brokers.

we just bought the domain for a website with www.homekeyfunding.example
that could be used in the design also.

On the business card would be
Front card:

Dale Whitcomb
Owner/Loan Officer
Cell: (555) 314-2297
Lending Harbor Partners
4172 Pinecrest Lane
Brookhaven, CA 93120
Office (555) 490-6631
Fax (555) 490-6674
website www.homekeyfunding.example

Back of Card:

LHP BRE #0378215 NMLS #586249
Dale Whitcomb BRE # 04519863 NMLS #587716

Industry/Entity Type

Business

```html
<!DOCTYPE html>
<html lang="en">
<head>
<meta charset="utf-8">
<title>Lending Harbor Partners – Business Cards</title>
<link rel="stylesheet" href="https://fonts.googleapis.com/css2?family=Cinzel:wght@500&family=Open+Sans:wght@400;600;700&display=swap">
<style>
  :root {
    --page-bg: #ece9e4;
    --navy-deep: #0d3f66;
    --navy-mid: #1b6aa6;
    --sky: #5aa6dc;
    --brand-blue: #1f6d9f;
    --brand-brown: #5a3a22;
    --text-brown: #4a3322;
    --ghost: #dfe5ee;
    --white: #ffffff;
    --card-shadow: 0 10px 28px rgba(0,0,0,0.22);
  }
  * { margin: 0; padding: 0; box-sizing: border-box; }
  html, body {
    width: 1200px; height: 784px; overflow: hidden;
    background: var(--page-bg);
    font-family: "Open Sans", Arial, sans-serif;
  }
  .canvas { position: relative; width: 1200px; height: 784px; }

  .card {
    position: absolute;
    width: 640px; height: 366px;
    border-radius: 4px;
    box-shadow: var(--card-shadow);
    overflow: hidden;
  }

  /* Back of card */
  .card-back { left: 60px; top: 56px; color: var(--white); }
  .card-back .pattern-field {
    position: absolute; inset: 0;
    background:
      radial-gradient(ellipse at 78% 30%, rgba(120,190,240,0.55), transparent 60%),
      linear-gradient(120deg, var(--navy-deep) 0%, var(--navy-mid) 55%, var(--sky) 100%);
  }
  .card-back .brand {
    position: absolute; left: 0; right: 0; top: 70px;
    text-align: center;
  }
  .card-back .brand-mark {
    font-family: "Cinzel", serif; font-weight: 500;
    font-size: 78px; letter-spacing: 4px; line-height: 1;
    color: #e4e9ef;
  }
  .card-back .brand-name {
    font-family: "Cinzel", serif; font-weight: 500;
    font-size: 21px; letter-spacing: 1px; margin-top: 8px;
    color: #e4e9ef;
  }
  .card-back .licenses {
    position: absolute; left: 0; right: 0; top: 240px;
    text-align: center; font-size: 17px; font-weight: 600;
    letter-spacing: 1.2px; line-height: 1.45;
  }

  /* Front of card */
  .card-front { left: 500px; top: 362px; background: var(--white); }
  .card-front .ghost-mark {
    position: absolute; right: 20px; top: 135px;
    font-family: "Cinzel", serif; font-weight: 500;
    font-size: 150px; line-height: 1; letter-spacing: 2px;
    color: var(--ghost);
  }
  .card-front .person {
    position: absolute; right: 22px; top: 16px; text-align: right;
  }
  .card-front .person-name {
    font-size: 16px; font-weight: 700; color: var(--brand-blue);
  }
  .card-front .person-title {
    font-size: 10.5px; color: #333; margin-top: 1px;
  }
  .card-front .brand {
    position: absolute; left: 34px; top: 60px;
  }
  .card-front .brand-mark {
    font-family: "Cinzel", serif; font-weight: 500;
    font-size: 66px; line-height: 1; letter-spacing: 3px;
    color: var(--brand-blue);
  }
  .card-front .brand-name {
    font-family: "Cinzel", serif; font-weight: 500;
    font-size: 17px; margin-top: 6px;
    color: var(--brand-brown);
  }
  .contact-list {
    position: absolute; left: 30px; top: 212px;
    list-style: none;
    font-size: 15.5px; color: var(--text-brown); line-height: 1.2;
  }
  .contact-list li { display: flex; align-items: flex-start; gap: 8px; margin-bottom: 1px; }
  .contact-list .icon { width: 17px; height: 17px; flex: none; margin-top: 1px; fill: var(--brand-blue); }
  .contact-list .spacer { width: 17px; flex: none; }
</style>
</head>
<body>
<main class="canvas">

  <section class="card card-back" aria-label="Back of business card">
    <div class="pattern-field" role="img" aria-label="Blue background with a receding pattern of soft light-blue dots"></div>
    <div class="brand">
      <div class="brand-mark">LHP</div>
      <div class="brand-name">Lending Harbor Partners</div>
    </div>
    <div class="licenses">
      <p>LHP BRE #0378215 NMLS #586249</p>
      <p>Dale Whitcomb BRE # 04519863 NMLS #587716</p>
    </div>
  </section>

  <section class="card card-front" aria-label="Front of business card">
    <div class="ghost-mark" aria-hidden="true">LHP</div>
    <div class="person">
      <p class="person-name">Dale Whitcomb</p>
      <p class="person-title">Owner/Loan Officer</p>
    </div>
    <div class="brand">
      <div class="brand-mark">LHP</div>
      <div class="brand-name">Lending Harbor Partners</div>
    </div>
    <ul class="contact-list">
      <li>
        <svg class="icon" viewBox="0 0 16 16" aria-hidden="true"><path d="M8 1 0.5 7.5h2V15h4.2v-4.5h2.6V15h4.2V7.5h2z"/></svg>
        <span>4172 Pinecrest Lane</span>
      </li>
      <li><span class="spacer"></span><span>Brookhaven, CA 93120</span></li>
      <li>
        <svg class="icon" viewBox="0 0 16 16" aria-hidden="true"><rect x="4" y="1" width="8" height="14" rx="1.5"/><rect x="5.5" y="3" width="5" height="7" fill="#fff"/></svg>
        <span>(555) 314-2297</span>
      </li>
      <li>
        <svg class="icon" viewBox="0 0 16 16" aria-hidden="true"><path d="M3.5 1.5 6 4 4.7 6.2c.9 2 2.4 3.5 4.4 4.4L11.3 9.3 14 11.8 12.4 14.5C6.5 14 2 9.5 1.5 3.6z"/></svg>
        <span>(555) 490-6631</span>
      </li>
      <li>
        <svg class="icon" viewBox="0 0 16 16" aria-hidden="true"><rect x="4" y="1" width="8" height="5" fill="none" stroke="#1f6d9f" stroke-width="1.4"/><rect x="1" y="6" width="14" height="7" rx="1.5"/><rect x="4" y="11" width="8" height="4" fill="#fff" stroke="#1f6d9f" stroke-width="1.2"/></svg>
        <span>(555) 490-6674</span>
      </li>
      <li>
        <svg class="icon" viewBox="0 0 16 16" aria-hidden="true"><circle cx="8" cy="8" r="7"/><path d="M1 8h14M8 1c-3 3-3 11 0 14M8 1c3 3 3 11 0 14M2.5 4.5h11M2.5 11.5h11" stroke="#fff" stroke-width="0.9" fill="none"/></svg>
        <span>www.homekeyfunding.example</span>
      </li>
    </ul>
  </section>

</main>
</body>
</html>
```